Tellbrook Mechanical Heating and Air Conditioning web page

This is a repair, installation and maintenance residential company. I don't do commercial. I need a web design that shows a company with 24/7 fast service that is easy for customers to contact me from. I am a Varnell /Oskiro HVAC dealer and their logos can be on there also. I also sell IAQ products like Zuvo- Crest and I offer duct cleanings as well.

Industry/Entity Type

Hvac

Coding

Coded - Design and coding required

Number of Pages Required

2 page

```html
<!DOCTYPE html>
<html lang="en">
<head>
<meta charset="utf-8">
<title>Tellbrook Mechanical – Heating and Air Conditioning</title>
<link rel="stylesheet" href="https://fonts.googleapis.com/css2?family=Michroma&family=Montserrat:wght@400;500;600;700&display=swap">
<style>
:root{
  --blue:#1a9de1;
  --red:#e41e26;
  --ink:#1b1b1b;
  --text:#3a3a3a;
  --muted:#6b6b6b;
  --light:#f1f1f1;
  --footer:#111214;
  --white:#ffffff;
  --display:'Michroma',sans-serif;
  --body:'Montserrat',sans-serif;
}
*{box-sizing:border-box;margin:0;padding:0}
html,body{width:1200px;height:4691px;overflow:hidden}
body{position:relative;font-family:var(--body);color:var(--text);background:var(--white)}
.abs{position:absolute}
.section{position:absolute;left:0;width:1200px;overflow:hidden}
.heading{font-family:var(--display);color:var(--ink);letter-spacing:2px;text-transform:uppercase;line-height:1.2}
.btn{position:absolute;display:flex;align-items:center;justify-content:center;border-radius:20px;color:var(--white);font-size:13px;font-weight:500}
.btn-blue{background:var(--blue)}
.btn-red{background:var(--red)}
.photo{position:absolute}

/* header */
.site-header{top:0;height:118px;background:var(--white)}
.brand{left:73px;top:22px;font-family:var(--display);color:var(--ink);font-size:25px;line-height:30px;letter-spacing:1px}
.contact-item{top:38px;display:flex;gap:10px;align-items:center}
.contact-item .dot{width:40px;height:40px;border-radius:50%;display:flex;align-items:center;justify-content:center}
.contact-item .label{font-family:var(--display);font-size:11px;letter-spacing:1px}
.contact-item .value{font-size:12px;color:var(--ink);margin-top:2px}

/* nav */
.main-nav{top:118px;height:55px;background:var(--blue)}
.nav-link{top:0;height:55px;display:flex;align-items:center;justify-content:center;color:var(--white);font-size:13px;transform:translateX(-50%)}
.nav-home{left:75px;width:120px;transform:none;background:var(--red)}
.nav-sep{top:14px;width:1px;height:27px;background:rgba(255,255,255,.35)}
.appt{left:932px;top:8px;width:192px;height:38px;border-radius:19px;background:var(--red);color:var(--white);font-size:12px;display:flex;align-items:center;justify-content:center;gap:8px}

/* hero */
.hero{top:173px;height:670px}
.hero-photo{left:0;top:0;width:1200px;height:670px;background:linear-gradient(180deg,#eef1f3 0%,#dfe5ea 45%,#b9c2c8 70%,#8f9aa2 100%)}
.hero-kicker{left:0;width:1200px;top:175px;text-align:center;font-family:var(--display);font-size:18px;color:var(--ink);letter-spacing:2px}
.hero-title{left:0;width:1200px;top:205px;text-align:center;font-family:var(--display);font-size:30px;color:var(--ink);letter-spacing:2px}
.slide-arrow{top:232px;width:38px;height:38px;border-radius:50%;display:flex;align-items:center;justify-content:center}
.badge{left:165px;top:500px;width:114px;height:114px;border-radius:50%;background:var(--blue);border:4px solid var(--white);color:var(--white);display:flex;flex-direction:column;align-items:center;justify-content:center;font-weight:700;line-height:1.05}
.badge .big{font-size:30px;font-style:normal}
.badge .small{font-size:13px}

/* about */
.about{top:800px;height:442px}
.about-photo{left:127px;top:20px;width:420px;height:422px;background:linear-gradient(160deg,#f5f5f5 0%,#e6e6e6 40%,#3c6ea8 60%,#c68a2f 85%)}
.about-title{left:518px;top:5px;font-size:28px}
.about-sub{left:506px;top:52px;font-size:11px;color:var(--ink)}
.about-kicker{left:574px;top:88px;display:flex;align-items:center;gap:22px;font-family:var(--display);font-size:16px;color:var(--ink);letter-spacing:1px}
.about-kicker .rule{width:60px;height:2px;background:var(--blue)}
.about-copy{left:630px;top:132px;width:463px;font-size:12.2px;line-height:1.25;color:var(--text)}
.about-copy p{margin-bottom:12px}

/* services */
.services{top:1242px;height:603px;background:var(--light)}
.section-title{left:0;width:1200px;text-align:center;font-size:28px}
.service-card{top:115px;height:360px;width:302px;background:var(--white);text-align:center}
.service-card .pic{position:absolute;left:10px;top:10px;width:282px;height:178px}
.service-card .icon{position:absolute;left:126px;top:164px;width:50px;height:50px;border-radius:50%;background:var(--white);display:flex;align-items:center;justify-content:center}
.service-card h3{position:absolute;top:220px;width:100%;font-family:var(--display);font-size:13px;line-height:16px;color:var(--ink);letter-spacing:1px;font-weight:400}
.service-card .rule{position:absolute;left:137px;top:243px;width:28px;height:2px;background:var(--blue)}
.service-card p{position:absolute;left:26px;top:256px;width:250px;font-size:11.2px;line-height:1.35}
.service-card .go{position:absolute;left:140px;top:320px;width:22px;height:22px;border-radius:50%;border:2px solid var(--ink)}
.service-card.featured{background:var(--red)}
.service-card.featured h3,.service-card.featured p{color:var(--white)}
.service-card.featured .rule{background:var(--white)}
.service-card.featured .icon{background:var(--red)}

/* heating band */
.heating{top:1845px;height:559px}
.heating-photo{left:0;top:0;width:1200px;height:559px;background:linear-gradient(90deg,#f4f4f4 0%,#eceeef 45%,#d7dcdf 75%,#a7b0b6 100%)}
.heating-title{left:111px;top:133px;font-size:26px}
.heating-copy{left:111px;top:207px;width:445px;font-size:12.2px;line-height:1.25}
.tick-item{left:111px;display:flex;align-items:center;gap:10px;font-size:12.5px;color:var(--ink)}

/* gallery */
.gallery{top:2404px;height:604px}
.divider{left:554px;top:100px;display:flex;align-items:center;gap:8px}
.divider .line{width:28px;height:2px;background:var(--blue)}
.tile{position:absolute}
.tile-overlay{background:#222426}
.tile-overlay h4{position:absolute;left:20px;top:70px;font-family:var(--display);font-size:14px;color:var(--white);letter-spacing:1px;font-weight:400}
.tile-overlay p{position:absolute;left:20px;top:100px;width:260px;font-size:11.5px;color:var(--white);line-height:1.3}
.tile-overlay .go{position:absolute;left:20px;top:142px;width:16px;height:16px;border-radius:50%;border:1.5px solid var(--white)}

/* blogs */
.blogs{top:3008px;height:958px}
.blog-card{top:140px;width:306px;height:348px;background:var(--white);border:1px solid #e4e4e4}
.blog-card .pic{position:absolute;left:0;top:0;width:100%;height:192px}
.blog-card .date{position:absolute;left:130px;top:168px;width:46px;height:46px;border-radius:50%;background:var(--red);color:var(--white);display:flex;flex-direction:column;align-items:center;justify-content:center;font-size:11px;line-height:1.15;border:3px solid var(--white)}
.blog-card h3{position:absolute;left:14px;top:232px;font-family:var(--display);font-size:11px;line-height:14px;color:var(--ink);letter-spacing:1px;font-weight:400}
.blog-card p{position:absolute;left:14px;top:256px;width:280px;font-size:11.5px;line-height:1.3}
.blog-card .more{position:absolute;left:14px;top:314px;font-size:11.5px;color:var(--ink);text-decoration:underline}
.testi-sub{left:0;width:1200px;top:666px;text-align:center;font-size:11px;color:var(--ink)}
.testi-photo{left:283px;top:708px;width:190px;height:212px;border-radius:50%;background:radial-gradient(circle at 50% 40%,#f0e4d6 0%,#d9cdbf 55%,#eef0f2 100%)}
.testi-name{left:510px;top:720px;font-family:var(--display);font-size:16px;color:var(--ink)}
.testi-role{left:510px;top:744px;font-size:13px;color:var(--red)}
.testi-text{left:510px;top:770px;width:490px;font-size:11.8px;line-height:1.25}
.stars{left:510px;top:838px;color:#f2a614;font-size:12px;letter-spacing:3px}
.pager{left:583px;top:916px;display:flex;gap:7px}
.pager span{width:7px;height:7px;border-radius:50%;background:#9a9a9a}
.pager span:first-child{background:var(--red)}

/* quote */
.quote{top:3966px;height:440px;background:linear-gradient(90deg,#e9ecef 0%,#f4f5f6 60%,#f6f6f6 100%)}
.quote-photo{left:0;top:0;width:600px;height:440px;background:linear-gradient(135deg,#f0f1f2 10%,#dcdfe2 50%,#c9cfd4 80%,#eef0f1 100%)}
.quote-title{left:643px;top:80px;font-size:27px}
.quote-intro{left:643px;top:125px;width:450px;font-size:11.8px;line-height:1.2}
.field{height:33px;background:var(--white);border:1px solid #dadada;font-size:11.5px;color:var(--text);padding-left:12px;display:flex;align-items:center}

/* footer */
.site-footer{top:4360px;height:265px}
.footer-body{left:0;top:0;width:1200px;height:265px}
.foot-brand{left:115px;top:120px;font-family:var(--display);color:var(--white);font-size:22px;line-height:28px;letter-spacing:1px}
.foot-head{font-family:var(--display);font-size:12px;color:var(--white);letter-spacing:1px}
.foot-list{list-style:none;font-size:12.5px;color:var(--white);line-height:22.5px}
.foot-list li::before{content:"›";margin-right:10px}
.contact-line{display:flex;gap:16px;font-size:12.5px;color:var(--white);line-height:26.5px}
.copyright{top:4625px;height:66px;background:var(--white)}
.copyright p{position:absolute;left:113px;top:24px;font-size:11px;color:var(--ink)}
.social{position:absolute;top:18px;width:27px;height:27px;border-radius:50%;background:var(--ink)}
.social.first{background:var(--blue)}
</style>
</head>
<body>

<header class="section site-header">
  <div class="abs brand">TELLBROOK<br>MECHANICAL</div>
  <div class="abs contact-item" style="left:608px">
    <div class="dot" style="background:var(--red)">
      <svg width="20" height="20" viewBox="0 0 20 20"><circle cx="10" cy="10" r="7.5" fill="none" stroke="#fff" stroke-width="2"/><path d="M10 5.5V10l3 2" fill="none" stroke="#fff" stroke-width="2" stroke-linecap="round"/></svg>
    </div>
    <div><div class="label" style="color:var(--red)">AVAILABLE</div><div class="value">24/7 Fast Service</div></div>
  </div>
  <div class="abs contact-item" style="left:808px">
    <div class="dot" style="background:var(--red)">
      <svg width="20" height="16" viewBox="0 0 20 16"><rect x="1" y="1" width="18" height="14" rx="2" fill="none" stroke="#fff" stroke-width="2"/><path d="M1.5 2l8.5 7 8.5-7" fill="none" stroke="#fff" stroke-width="2"/></svg>
    </div>
    <div><div class="label" style="color:var(--red)">EMAIL US</div><div class="value">info@tellbrook.com</div></div>
  </div>
  <div class="abs contact-item" style="left:993px">
    <div class="dot" style="background:var(--blue)">
      <svg width="18" height="18" viewBox="0 0 24 24"><path d="M6.6 10.8c1.4 2.8 3.8 5.1 6.6 6.6l2.2-2.2c.3-.3.7-.4 1-.2 1.1.4 2.3.6 3.6.6.6 0 1 .4 1 1V20c0 .6-.4 1-1 1C10.6 21 3 13.4 3 4c0-.6.4-1 1-1h3.5c.6 0 1 .4 1 1 0 1.3.2 2.5.6 3.6.1.3 0 .7-.2 1z" fill="#fff"/></svg>
    </div>
    <div><div class="label" style="color:var(--blue)">CALL US</div><div class="value">555 214 8630</div></div>
  </div>
</header>

<nav class="section main-nav">
  <div class="abs nav-link nav-home">Home</div>
  <div class="abs nav-link" style="left:264px">About us</div>
  <div class="abs nav-sep" style="left:338px"></div>
  <div class="abs nav-link" style="left:422px">Our Services&nbsp;˅</div>
  <div class="abs nav-sep" style="left:502px"></div>
  <div class="abs nav-link" style="left:561px">Gallery</div>
  <div class="abs nav-sep" style="left:620px"></div>
  <div class="abs nav-link" style="left:679px">Blog</div>
  <div class="abs nav-sep" style="left:740px"></div>
  <div class="abs nav-link" style="left:810px">Contact us</div>
  <div class="abs appt">
    <svg width="13" height="13" viewBox="0 0 14 14"><rect x="1" y="2.5" width="12" height="10.5" rx="1" fill="none" stroke="#fff" stroke-width="1.5"/><path d="M1 6h12M4 1v3M10 1v3" stroke="#fff" stroke-width="1.5"/></svg>
    Make an Appoinment
  </div>
</nav>

<section class="section hero">
  <div class="photo hero-photo" role="img" aria-label="Bright living room with a wall air conditioner, a woman reading with a remote and a man working on a laptop on a grey sofa"></div>
  <div class="abs hero-kicker">WELCOME TO</div>
  <div class="abs hero-title">TELLBROOK MECHANICAL</div>
  <div class="abs slide-arrow" style="left:19px;background:rgba(255,255,255,.8)">
    <svg width="10" height="12" viewBox="0 0 10 12"><path d="M7 1L2 6l5 5" fill="none" stroke="#333" stroke-width="1.6"/></svg>
  </div>
  <div class="abs slide-arrow" style="left:1145px;background:var(--red)">
    <svg width="10" height="12" viewBox="0 0 10 12"><path d="M3 1l5 5-5 5" fill="none" stroke="#fff" stroke-width="1.8"/></svg>
  </div>
  <svg class="abs" style="left:0;top:500px" width="1200" height="170" viewBox="0 0 1200 170" preserveAspectRatio="none">
    <path d="M0 170 C 200 60, 600 25, 1200 15 L1200 170 Z" fill="var(--red)"/>
    <path d="M0 170 C 40 150, 200 90, 420 70 C 700 45, 1000 35, 1200 30 L1200 170 Z" fill="#fff"/>
  </svg>
  <div class="abs badge"><span class="big">24/7</span><span class="small">FAST</span><span class="small">SERVICE</span></div>
</section>

<section class="section about">
  <div class="photo about-photo" role="img" aria-label="HVAC technician in a hard hat holding a clipboard beside an outdoor unit and an indoor split air conditioner"></div>
  <h2 class="abs heading about-title">ABOUT US</h2>
  <div class="abs about-sub">Lorem Ipsum is simply dummy text</div>
  <div class="abs about-kicker"><span class="rule"></span>WHAT IS LOREM IPSUM?</div>
  <div class="abs about-copy">
    <p>Lorem Ipsum is a simply dummy text of the printing and typesetting an industry has been the industry's standard an dummy text ever since the 1500s,</p>
    <p>when an unknown printer took a galley of type and scrambled it to make a type specimen book. It has survived not only five centuries, but also the leap into electronic typesetting, remaining essentially unchanged was popularised in the 1960s</p>
    <p>with the release of Typeline sheets containing Lorem Ipsum passages, and more recently with desktop publishing software like Pagemill Draft including versions of Lorem Ipsum.</p>
  </div>
  <div class="btn btn-blue" style="left:630px;top:348px;width:158px;height:37px">Read More</div>
</section>

<section class="section services">
  <h2 class="abs heading section-title" style="top:60px">SERVICES</h2>

  <article class="abs service-card" style="left:113px">
    <div class="pic" role="img" aria-label="Man relaxing with a laptop under a wall air conditioner" style="background:linear-gradient(160deg,#f2f3f4,#c9cfd3)"></div>
    <div class="icon"><svg width="24" height="22" viewBox="0 0 24 22"><path d="M12 1L1 11h3v10h6v-6h4v6h6V11h3z" fill="var(--ink)"/></svg></div>
    <h3>RESIDENTIAL</h3><span class="rule"></span>
    <p>Lorem Ipsum is a simply dummy text of the printing and typesetting industry it has been dummy text ever since the 1500s,</p>
    <span class="go"></span>
  </article>

  <article class="abs service-card featured" style="left:452px">
    <div class="pic" role="img" aria-label="Technician tool bag with refrigerant pressure gauges" style="background:linear-gradient(160deg,#7b5a3e,#2e6b4a 60%,#c8cdd1)"></div>
    <div class="icon"><svg width="22" height="22" viewBox="0 0 24 24"><path d="M20.7 14.3l-5-5 1.6-1.6a3.5 3.5 0 00-4.9-4.9L10.8 4.4l3.6 3.6-2.1 2.1L8.7 6.5 7.1 8.1a3.5 3.5 0 004.9 4.9L13.6 11l5 5a1.5 1.5 0 002.1-2.1zM3 21l6-6" fill="#fff" stroke="#fff" stroke-width="1.5"/></svg></div>
    <h3>REPAIR</h3><span class="rule"></span>
    <p>Lorem Ipsum is a simply dummy text of the printing and typesetting industry it has been dummy text ever since the 1500s,</p>
  </article>

  <article class="abs service-card" style="left:787px">
    <div class="pic" role="img" aria-label="Technician installing a wall-mounted air conditioner" style="background:linear-gradient(160deg,#eeeff0,#c3c9ce 60%,#4e6fa0)"></div>
    <div class="icon"><svg width="22" height="22" viewBox="0 0 24 24"><path d="M12 2l1.6 2.7 3-.8.8 3 2.7 1.6-1.4 2.5 1.4 2.5-2.7 1.6-.8 3-3-.8L12 22l-1.6-2.7-3 .8-.8-3-2.7-1.6L5.3 12 3.9 9.5l2.7-1.6.8-3 3 .8z" fill="var(--ink)"/><circle cx="12" cy="12" r="3.2" fill="#fff"/></svg></div>
    <h3>INSTALLATION</h3><span class="rule"></span>
    <p>Lorem Ipsum is a simply dummy text of the printing and typesetting industry it has been dummy text ever since the 1500s,</p>
    <span class="go"></span>
  </article>

  <div class="btn btn-blue" style="left:515px;top:512px;width:159px;height:37px">View More</div>
</section>

<section class="section heating">
  <div class="photo heating-photo" role="img" aria-label="Man on a grey sofa with a laptop, pointing a remote at a wall air conditioner"></div>
  <h2 class="abs heading heating-title">HEATING &amp; AIR CONDITIONING</h2>
  <p class="abs heating-copy">Lorem Ipsum is a simply dummy text of the printing and typesetting an industry has been the industry's standard an dummy text ever since the 1500s,</p>
  <div class="abs tick-item" style="top:270px">
    <svg width="18" height="18" viewBox="0 0 18 18"><circle cx="9" cy="9" r="8" fill="none" stroke="var(--red)" stroke-width="1.5"/><path d="M5 9l3 3 6-7" fill="none" stroke="var(--red)" stroke-width="2"/></svg>Cool Air
  </div>
  <div class="abs tick-item" style="top:297px">
    <svg width="18" height="18" viewBox="0 0 18 18"><circle cx="9" cy="9" r="8" fill="none" stroke="var(--red)" stroke-width="1.5"/><path d="M5 9l3 3 6-7" fill="none" stroke="var(--red)" stroke-width="2"/></svg>Speedy service
  </div>
  <div class="btn btn-blue" style="left:111px;top:349px;width:158px;height:37px">View More</div>
  <div class="btn btn-red" style="left:291px;top:349px;width:158px;height:37px">Contact us</div>
</section>

<section class="section gallery">
  <h2 class="abs heading section-title" style="top:50px">GALLERY</h2>
  <div class="abs divider">
    <span class="line"></span>
    <svg width="22" height="22" viewBox="0 0 22 22"><g stroke="var(--blue)" stroke-width="2" stroke-linecap="round"><path d="M11 2v18M3.2 6.5l15.6 9M3.2 15.5l15.6-9"/></g></svg>
    <span class="line"></span>
  </div>
  <div class="tile" role="img" aria-label="Technician reading refrigerant gauges on an outdoor unit" style="left:113px;top:131px;width:309px;height:165px;background:linear-gradient(150deg,#c0c7cd,#3f5670 60%,#9aa3ab)"></div>
  <div class="tile tile-overlay" style="left:113px;top:318px;width:309px;height:168px">
    <h4>PROJECT TITLE</h4>
    <p>Lorem Ipsum is simply dummy text type set int the world industry.</p>
    <span class="go"></span>
  </div>
  <div class="tile" role="img" aria-label="Woman sitting on the floor enjoying cool air from a wall unit" style="left:444px;top:131px;width:310px;height:355px;background:linear-gradient(180deg,#f1efec,#d9d4ce 55%,#a7b5c5)"></div>
  <div class="tile" role="img" aria-label="Hand holding an air conditioner remote control" style="left:776px;top:131px;width:309px;height:165px;background:linear-gradient(150deg,#e9ecee,#c6ccd0)"></div>
  <div class="tile" role="img" aria-label="Woman working at a desk in a bright office" style="left:776px;top:318px;width:309px;height:168px;background:linear-gradient(150deg,#f3f2ef,#d5d2cc 60%,#8a8c90)"></div>
  <div class="btn btn-blue" style="left:522px;top:515px;width:158px;height:37px">View More</div>
</section>

<section class="section blogs">
  <h2 class="abs heading section-title" style="top:82px">BLOGS</h2>

  <article class="abs blog-card" style="left:113px">
    <div class="pic" role="img" aria-label="Technician repairing the open housing of an indoor unit" style="background:linear-gradient(150deg,#c7cdd2,#e6e8ea 50%,#b84a3c)"></div>
    <div class="date"><b>14</b>Apr</div>
    <h3>WHAT IS LOREM IPSUM?</h3>
    <p>Lorem Ipsum is simply dummy text the printing and typesetting industry Lorem Ipsum has been dummy text ever since the 1500s,</p>
    <span class="more">Continue..</span>
  </article>
  <article class="abs blog-card" style="left:446px">
    <div class="pic" role="img" aria-label="Woman standing under a wall air conditioner in a living room" style="background:linear-gradient(180deg,#eff0f0,#d7d9db 60%,#5a5f64)"></div>
    <div class="date"><b>14</b>Apr</div>
    <h3>WHAT IS LOREM IPSUM?</h3>
    <p>Lorem Ipsum is simply dummy text the printing and typesetting industry Lorem Ipsum has been dummy text ever since the 1500s,</p>
    <span class="more">Continue..</span>
  </article>
  <article class="abs blog-card" style="left:779px">
    <div class="pic" role="img" aria-label="Technician cleaning the filter of an indoor unit" style="background:linear-gradient(150deg,#e3e6e8,#9aa6b0 50%,#2e3b52)"></div>
    <div class="date"><b>14</b>Apr</div>
    <h3>WHAT IS LOREM IPSUM?</h3>
    <p>Lorem Ipsum is simply dummy text the printing and typesetting industry Lorem Ipsum has been dummy text ever since the 1500s,</p>
    <span class="more">Continue..</span>
  </article>
  <div class="btn btn-blue" style="left:522px;top:519px;width:158px;height:37px">View More</div>

  <h2 class="abs heading section-title" style="top:622px">TESTIMONIALS</h2>
  <div class="abs testi-sub">What Clients say about us</div>
  <svg class="abs" style="left:196px;top:778px" width="18" height="30" viewBox="0 0 18 30"><path d="M15 2L3 15l12 13" fill="none" stroke="#c8c8c8" stroke-width="2"/></svg>
  <svg class="abs" style="left:1034px;top:778px" width="18" height="30" viewBox="0 0 18 30"><path d="M3 2l12 13L3 28" fill="none" stroke="#c8c8c8" stroke-width="2"/></svg>
  <span class="abs" style="left:250px;top:700px;width:18px;height:18px;border-radius:50%;background:var(--red)"></span>
  <span class="abs" style="left:272px;top:704px;width:10px;height:10px;border-radius:50%;background:var(--red)"></span>
  <span class="abs" style="left:256px;top:722px;width:8px;height:8px;border-radius:50%;background:var(--red)"></span>
  <div class="abs" style="left:254px;top:734px;width:26px;height:26px;border-radius:50%;background:var(--blue);color:#fff;font-size:18px;font-weight:700;display:flex;align-items:center;justify-content:center">“</div>
  <div class="abs testi-photo" role="img" aria-label="Portrait of a smiling client in a blazer"></div>
  <div class="abs testi-name">Clara Whitfield</div>
  <div class="abs testi-role">Creative Director</div>
  <p class="abs testi-text">Lorem Ipsum&nbsp; simply dummy text the printing and ypesetting industry simply an dummy Ipsum is simply dummy text of the printing.Lorem Ipsum&nbsp; simply dummy text the printing and industry&nbsp; simply dummy Ipsum is simply dummy text of the in the industries printing.</p>
  <div class="abs stars">★★★★★</div>
  <div class="abs pager"><span></span><span></span><span></span></div>
</section>

<section class="section quote">
  <div class="photo quote-photo" role="img" aria-label="Man in a white shirt pointing a remote at an air conditioner beside a potted plant"></div>
  <h2 class="abs heading quote-title">REQUEST A QUOTE</h2>
  <p class="abs quote-intro">Lorem Ipsum&nbsp; simply dummy text the printing and ypesetting and dummy Ipsum is simply dummy text of the printing.</p>
  <div class="abs field" style="left:643px;top:177px;width:207px">First Name</div>
  <div class="abs field" style="left:861px;top:177px;width:210px">Last Name</div>
  <div class="abs field" style="left:643px;top:221px;width:207px">Phone</div>
  <div class="abs field" style="left:861px;top:221px;width:210px">Email</div>
  <div class="abs field" style="left:643px;top:266px;width:428px;justify-content:space-between;padding-right:12px">Interested in<span style="font-size:9px">˅</span></div>
  <div class="btn btn-blue" style="left:641px;top:315px;width:157px;height:36px">Send Now</div>
</section>

<footer class="section site-footer">
  <svg class="abs footer-body" width="1200" height="265" viewBox="0 0 1200 265" preserveAspectRatio="none">
    <path d="M0 60 C 300 20, 700 10, 1200 28 L1200 265 L0 265 Z" fill="var(--red)"/>
    <path d="M0 175 C 120 120, 320 70, 600 55 C 850 42, 1050 40, 1200 44 L1200 265 L0 265 Z" fill="var(--footer)"/>
  </svg>
  <div class="abs foot-brand">TELLBROOK<br>MECHANICAL</div>

  <div class="abs foot-head" style="left:402px;top:65px">QUICK LINKS</div>
  <ul class="abs foot-list" style="left:402px;top:91px">
    <li>Home</li><li>About us</li><li>Our Services</li><li>Gallery</li><li>Blog</li><li>Contact us</li>
  </ul>

  <div class="abs foot-head" style="left:614px;top:65px">CONTACT INFORMATION</div>
  <div class="abs" style="left:614px;top:89px">
    <div class="contact-line"><svg width="12" height="26" viewBox="0 0 24 24"><path d="M6.6 10.8c1.4 2.8 3.8 5.1 6.6 6.6l2.2-2.2c.3-.3.7-.4 1-.2 1.1.4 2.3.6 3.6.6.6 0 1 .4 1 1V20c0 .6-.4 1-1 1C10.6 21 3 13.4 3 4c0-.6.4-1 1-1h3.5c.6 0 1 .4 1 1 0 1.3.2 2.5.6 3.6.1.3 0 .7-.2 1z" fill="#fff"/></svg>(00) 555 214 8630</div>
    <div class="contact-line"><svg width="12" height="26" viewBox="0 0 20 16"><rect x="1" y="1" width="18" height="14" fill="#fff"/><path d="M1.5 2l8.5 7 8.5-7" fill="none" stroke="#111" stroke-width="2"/></svg>info@tellbrook.com</div>
    <div class="contact-line"><svg width="12" height="26" viewBox="0 0 16 22"><path d="M8 1a7 7 0 00-7 7c0 5 7 13 7 13s7-8 7-13a7 7 0 00-7-7zm0 9.5A2.5 2.5 0 118 5.5a2.5 2.5 0 010 5z" fill="#fff"/></svg>4780 Alder Street</div>
    <div class="contact-line" style="padding-left:28px">Fernvale, KY, Kentucky</div>
    <div class="contact-line" style="padding-left:28px">ZipCode : 40971</div>
  </div>

  <div class="abs foot-head" style="left:876px;top:65px">JOIN OUR MAILING LIST</div>
  <p class="abs" style="left:876px;top:85px;width:215px;font-size:11.5px;color:#fff;line-height:1.2">Lorem Ipsum&nbsp; simply dummy text typesetting and dummy.</p>
  <div class="abs field" style="left:876px;top:131px;width:211px;height:32px">Your Email</div>
  <div class="btn btn-blue" style="left:876px;top:174px;width:211px;height:32px">Submit</div>
</footer>

<div class="section copyright">
  <p>Copyright © 2020 Tellbrook Mechanical. All Right Reserved</p>
  <span class="social first" style="left:955px" aria-label="Social profile"></span>
  <span class="social" style="left:990px" aria-label="Social profile"></span>
  <span class="social" style="left:1024px" aria-label="Social profile"></span>
  <span class="social" style="left:1059px" aria-label="Social profile"></span>
</div>

</body>
</html>
```